Vex

I have the logo for the back already. Need the front to match.
Need a VEX logo which I can provide or you can download one - VEX Realty in canada... Back of the card will be my logo and name. Front will have the info...
I would like a black background. Match colors on front to the back..
Details on Card

Target Market(s)

Realestate clients.. Keep it classy like the logo

Contact Information for Business Card

Moren Tadwick office - 5817730264 cell - 5819063147 email - Moren@MorenTadwick.Com. website - MorenTadwick.Com Facebook - MTadwRealty Instagram - Moren_Qpl_Realtor Address - 418 - 23 St NE | K5P2M8

Colors
3176b5
33a6d7
85cae6

Requirements
Must have
• same color scheme as the logo
logo will be on the back
Black Background
Horizontal card
The one side of the card should be clean. like I stated, just my logo " Moren Tadwick " and nothing else

```html
<!DOCTYPE html>
<html lang="en">
<head>
<meta charset="UTF-8">
<title>Moren Tadwick – Business Card</title>
<link href="https://fonts.googleapis.com/css2?family=Cinzel:wght@500&family=Montserrat:wght@400&display=swap" rel="stylesheet">
<style>
  :root {
    --backdrop: #a3a3a3;
    --card-front: #151516;
    --card-back: #111213;
    --emboss: #0a0a0a;
    --brand-blue: #1a75bc;
    --band-text: #0d0d0d;
  }
  html, body {
    margin: 0;
    padding: 0;
    width: 1200px;
    height: 965px;
    overflow: hidden;
    background: var(--backdrop);
  }
  .canvas {
    position: relative;
    width: 1200px;
    height: 965px;
  }
  .card {
    position: absolute;
    left: 278px;
    width: 647px;
    height: 368px;
    border-radius: 24px;
    overflow: hidden;
  }
  .card--front {
    top: 98px;
    background: var(--card-front);
  }
  .card--back {
    top: 504px;
    background: var(--card-back);
  }
  .front-name {
    position: absolute;
    left: 0;
    right: 0;
    top: 150px;
    text-align: center;
    font-family: "Cinzel", serif;
    font-weight: 500;
    font-size: 52px;
    letter-spacing: 1px;
    color: var(--emboss);
  }
  .back-name {
    position: absolute;
    left: 20px;
    width: 340px;
    top: 160px;
    text-align: center;
    font-family: "Cinzel", serif;
    font-weight: 500;
    font-size: 27px;
    color: var(--brand-blue);
  }
  .divider {
    position: absolute;
    left: 320px;
    top: 118px;
    width: 2px;
    height: 132px;
    background: var(--brand-blue);
  }
  .contact-list {
    position: absolute;
    left: 348px;
    top: 114px;
    margin: 0;
    padding: 0;
    list-style: none;
    font-family: "Montserrat", sans-serif;
    font-size: 17.5px;
    color: var(--brand-blue);
  }
  .contact-list li {
    display: flex;
    align-items: center;
    height: 23.2px;
  }
  .contact-list svg {
    width: 16px;
    height: 16px;
    margin-right: 11px;
    flex: none;
  }
  .address-band {
    position: absolute;
    left: 0;
    top: 265px;
    width: 647px;
    height: 42px;
  }
  .band-segment {
    position: absolute;
    top: 0;
    height: 42px;
    background: var(--brand-blue);
  }
  .band-segment--left { left: 0; width: 68px; }
  .band-segment--mid {
    left: 126px;
    width: 392px;
    display: flex;
    align-items: center;
    justify-content: center;
    font-family: "Montserrat", sans-serif;
    font-size: 16px;
    color: var(--band-text);
  }
  .band-segment--right { left: 579px; width: 68px; }
  .brokerage-name {
    position: absolute;
    left: 68px;
    width: 58px;
    top: 0;
    height: 42px;
    display: flex;
    align-items: center;
    justify-content: center;
    text-align: center;
    font-family: "Cinzel", serif;
    font-weight: 500;
    font-size: 10px;
    line-height: 1.1;
    color: var(--brand-blue);
  }
  .band-mark {
    position: absolute;
    left: 518px;
    width: 61px;
    top: 0;
    height: 42px;
    display: flex;
    align-items: center;
    justify-content: center;
    text-align: center;
    font-family: "Cinzel", serif;
    font-weight: 500;
    font-size: 10px;
    line-height: 1.1;
    color: var(--brand-blue);
  }
</style>
</head>
<body>
<main class="canvas">
  <section class="card card--front" aria-label="Card front">
    <div class="front-name">MOREN TADWICK</div>
  </section>

  <section class="card card--back" aria-label="Card back">
    <div class="back-name">MOREN TADWICK</div>
    <div class="divider"></div>

    <ul class="contact-list">
      <li>
        <svg viewBox="0 0 16 16" aria-hidden="true"><path d="M3.5 1.5l2.5 0 1 3.5-1.8 1.2c.8 1.8 2.1 3.1 3.9 3.9L10.3 8.3l3.5 1v2.5c0 1-1 1.9-2 1.8C6.3 13.2 2.8 9.7 2 4.2 1.9 3 2.6 1.5 3.5 1.5z" fill="currentColor"/></svg>
        5817730264
      </li>
      <li>
        <svg viewBox="0 0 16 16" aria-hidden="true"><rect x="4" y="1" width="8" height="14" rx="1.5" fill="none" stroke="currentColor" stroke-width="1.6"/><rect x="7" y="12" width="2" height="1.4" fill="currentColor"/></svg>
        5819063147
      </li>
      <li>
        <svg viewBox="0 0 16 16" aria-hidden="true"><rect x="1.5" y="1.5" width="13" height="13" rx="2" fill="currentColor"/></svg>
        MTadwRealty
      </li>
      <li>
        <svg viewBox="0 0 16 16" aria-hidden="true"><circle cx="8" cy="8" r="6.5" fill="currentColor"/></svg>
        Moren_Qpl_Realtor
      </li>
      <li>
        <svg viewBox="0 0 16 16" aria-hidden="true"><rect x="1" y="3.5" width="14" height="9.5" fill="currentColor"/><path d="M1 3.8l7 5 7-5" fill="none" stroke="var(--card-back)" stroke-width="1.2"/></svg>
        Moren@MorenTadwick.Com
      </li>
      <li>
        <svg viewBox="0 0 16 16" aria-hidden="true"><circle cx="8" cy="8" r="6.5" fill="none" stroke="currentColor" stroke-width="1.5"/><ellipse cx="8" cy="8" rx="2.8" ry="6.5" fill="none" stroke="currentColor" stroke-width="1.2"/><line x1="1.5" y1="8" x2="14.5" y2="8" stroke="currentColor" stroke-width="1.2"/></svg>
        www.MorenTadwick.Com
      </li>
    </ul>

    <div class="address-band">
      <div class="band-segment band-segment--left"></div>
      <div class="brokerage-name">VEX<br>Realty</div>
      <div class="band-segment band-segment--mid">418 - 23 St NE | K5P2M8</div>
      <div class="band-mark">Moren<br>Tadwick</div>
      <div class="band-segment band-segment--right"></div>
    </div>
  </section>
</main>
</body>
</html>
```